Sunny Meadow coconut milk label design

We need a label design for our new line of coconut milk. Leaning towards a happy, healthy, and natural theme, but we are open for suggestions. We have several brand ideas in mind, but at the moment sunny meadow stands out. The product is in 400 ml cans, so the label wraps arounds the can as a finished product. Our can offers easy open lid as an advantage over our competitors, maybe a good idea to emphasize. Physical printed label dimension W24.5 cm (1 cm to the right is for foldover) x L10.3 cm. visit our site for an idea of the products, and see our existing products. www.loviterexports.example

Label design must consider areas for:
1. QR code
2. Nutrition Facts
3. General text information

attached is a sample design of our lotus pal label which targets ethnic markets. This new label is for an international mainstream and modern demographic.
Updates

Thanks to all designers for contributing in the last few days. The reality of a weekend deadline is causing us delay in providing all the necessary info on the label. As a result I have decided to extend this project by 5 days. I will update all the required label info soon. For already submitted designed please pay attention to these info and add them for final review. Designers who have not submit yet due to weekend disruptions will have 5 whole working days to submit. Thanks to all designers for participating. All your work and input are highly valued and appreciated. Cheers

Target Market(s)

Health conscious, vegetarian, lactose intolerant, metabolism boosting

Industry/Entity Type

Grocery

Font styles to use
Sans Serif

Colors

Designer to choose colors to be used in the design.

Requirements
Must have
• A happy, healthy, natural theme
Should not have
• health claims

```html
<!DOCTYPE html>
<html lang="en">
<head>
<meta charset="utf-8">
<title>Sunny Meadow Coconut Milk Label</title>
<link rel="stylesheet" href="https://fonts.googleapis.com/css2?family=Questrial&family=Raleway:wght@200&display=swap">
<style>
  :root {
    --brand-green: #05a10c;
    --ink: #111111;
    --paper: #ffffff;
  }
  html, body {
    margin: 0;
    padding: 0;
    width: 1200px;
    height: 291px;
    overflow: hidden;
    background: var(--paper);
  }
  .label {
    display: block;
    width: 1200px;
    height: 291px;
  }
  .brand-name {
    font-family: "Questrial", sans-serif;
    font-size: 27px;
    fill: var(--brand-green);
  }
  .product-name {
    font-family: "Raleway", sans-serif;
    font-weight: 200;
    font-size: 78px;
    fill: var(--ink);
  }
  .tagline {
    font-family: "Questrial", sans-serif;
    font-size: 29px;
    fill: var(--brand-green);
  }
  .badge-text {
    font-family: "Questrial", sans-serif;
    font-size: 10.5px;
    fill: var(--ink);
  }
  .rule { fill: var(--brand-green); }
  .mascot-area { fill: var(--brand-green); }
  .badge-ring {
    fill: var(--paper);
    stroke: var(--brand-green);
    stroke-width: 5.5;
  }
</style>
</head>
<body>
<svg class="label" viewBox="0 0 1200 291" xmlns="http://www.w3.org/2000/svg">
  <text class="brand-name" x="424" y="80" textLength="212" lengthAdjust="spacingAndGlyphs">SUNNY MEADOW</text>

  <rect class="mascot-area" x="648" y="26" width="176" height="80" rx="10"
        role="img" aria-label="Illustration of a smiling cow standing on the top rule"/>

  <rect class="rule" x="368" y="91" width="474" height="7.5" rx="2"/>

  <text class="product-name" x="330" y="180" textLength="544" lengthAdjust="spacingAndGlyphs">COCONUT MILK</text>

  <rect class="rule" x="368" y="208" width="474" height="8" rx="2"/>

  <text class="tagline" x="514" y="258" textLength="164" lengthAdjust="spacingAndGlyphs">100% Natural</text>

  <g class="easy-open-badge">
    <ellipse class="badge-ring" cx="764" cy="248" rx="54" ry="44"/>
    <text class="badge-text" x="764" y="240" text-anchor="middle">WITH EASY</text>
    <text class="badge-text" x="764" y="255" text-anchor="middle">TO OPEN LID</text>
  </g>
</svg>
</body>
</html>
```